New Book Cover Design Project

Book Cover with this title and sub title
Lessons Taught by the Old Orchard Hives
A pocket guide to careful spending and caring for nature.
Walter P. Kolb Ph. D.
Ruth P. Kolb
Picture below would be on the entire front cover. Words somehow incorporated for easy reading.

```html
<!DOCTYPE html>
<html lang="en">
<head>
<meta charset="utf-8">
<title>Lessons Taught by the Old Orchard Hives — Cover Wrap</title>
<link href="https://fonts.googleapis.com/css2?family=Poppins:wght@300;400;700;800&display=swap" rel="stylesheet">
<style>
  :root {
    --page: #ffffff;
    --green-light: #5f9b3d;
    --green-mid: #4a7d33;
    --green-deep: #3b652c;
    --band: #3a5c2c;
    --spine: #3a5c2c;
    --front-bg: #43712f;
    --white: #ffffff;
    --yellow: #f6e200;
    --bloom: #f3d51a;
    --bloom-deep: #e7b410;
  }
  * { box-sizing: border-box; margin: 0; padding: 0; }
  html, body {
    width: 1200px; height: 1200px; overflow: hidden;
    background: var(--page);
    font-family: "Poppins", sans-serif;
  }
  .wrap {
    position: absolute; left: 69px; top: 221px;
    width: 1070px; height: 767px;
    box-shadow: 0 6px 22px rgba(0,0,0,0.28);
  }
  .back-cover {
    position: absolute; left: 0; top: 0; width: 516px; height: 706px;
    background: radial-gradient(ellipse at 10% 0%, var(--green-light) 0%, var(--green-mid) 50%, var(--green-deep) 100%);
    overflow: hidden;
  }
  .back-bloom {
    position: absolute; left: -40px; top: 500px; width: 330px; height: 240px;
    background: radial-gradient(ellipse at 45% 55%, var(--bloom) 0%, rgba(243,213,26,0.75) 35%, rgba(243,213,26,0) 70%);
    filter: blur(6px);
  }
  .back-title {
    position: absolute; left: 0; width: 516px; top: 50px;
    text-align: center; color: var(--white); font-weight: 700;
    font-size: 26px; line-height: 30px; text-transform: uppercase;
  }
  .back-title .accent { display: block; color: var(--yellow); font-size: 40px; line-height: 42px; }
  .back-blurb {
    position: absolute; left: 42px; top: 192px; width: 427px;
    color: var(--white); font-size: 10.9px; line-height: 14.2px;
    text-align: justify; font-weight: 400;
  }
  .back-blurb p + p { margin-top: 17px; }
  .spine {
    position: absolute; left: 516px; top: 0; width: 38px; height: 767px;
    background: var(--spine); color: var(--white);
  }
  .spine-title, .spine-authors {
    position: absolute; writing-mode: vertical-rl; font-weight: 700;
    text-transform: uppercase; white-space: nowrap;
  }
  .spine-title { left: 8px; top: 41px; font-size: 13.5px; letter-spacing: 0.1px; }
  .spine-authors { left: 3px; top: 513px; font-size: 12.5px; line-height: 16px; }
  .front-cover {
    position: absolute; left: 554px; top: 0; width: 516px; height: 706px;
    background: var(--front-bg); overflow: hidden;
  }
  .front-photo {
    position: absolute; left: 0; top: 266px; width: 516px; height: 440px;
    background:
      radial-gradient(ellipse at 60% 75%, var(--bloom-deep) 0%, var(--bloom) 40%, rgba(243,213,26,0.9) 60%, rgba(67,113,47,0) 78%),
      var(--front-bg);
  }
  .front-title {
    position: absolute; left: 0; width: 516px; top: 38px;
    text-align: center; color: var(--white); font-weight: 700;
    text-transform: uppercase; font-size: 38px; line-height: 47px;
  }
  .front-title .accent { display: block; color: var(--yellow); font-size: 68px; line-height: 70px; }
  .front-subtitle {
    position: absolute; left: 20px; width: 476px; top: 208px;
    text-align: center; color: var(--white); font-weight: 300;
    font-size: 23px; line-height: 26px;
  }
  .author-band {
    position: absolute; left: 0; top: 706px; width: 1070px; height: 61px;
    background: var(--band);
  }
  .front-authors {
    position: absolute; left: 554px; width: 516px; top: 723px;
    text-align: center; color: var(--white); font-weight: 700;
    font-size: 21px; line-height: 26px; text-transform: uppercase; white-space: nowrap;
  }
  .front-authors .divider { margin: 0 12px; font-weight: 400; }
</style>
</head>
<body>
  <div class="wrap">
    <section class="back-cover">
      <div class="back-bloom" role="img" aria-label="Soft out-of-focus yellow flower in the corner"></div>
      <h2 class="back-title">Lessons Taught<br>by the Old Orchard<span class="accent">Hives</span></h2>
      <div class="back-blurb">
        <p>Lorem ipsum dolor sit amet, consectetur adipisicing elit, sed do eiusmod tempor incididunt ut labore et dolore magna aliqua. Ut enim ad minim veniam, quis nostrud exercitation ullamco laboris nisi ut aliquip ex ea commodo consequat. Duis aute irure dolor in reprehenderit in voluptate velit esse cillum dolore eu fugiat nulla pariatur. Excepteur sint occaecat cupidatat non proident, sunt in culpa qui officia deserunt mollit anim id est laborum. Sed ut perspiciatis unde omnis iste natus error sit voluptatem accusantium doloremque laudantium, totam rem aperiam, eaque ipsa quae ab illo inventore veritatis et quasi architecto beatae vitae dicta sunt explicabo. Nemo enim ipsam voluptatem quia voluptas sit aspernatur aut odit aut fugit, sed quia consequuntur magni dolores eos qui ratione voluptatem sequi nesciunt. Neque porro quisquam est, qui dolorem ipsum quia dolor sit amet, consectetur, adipisci velit, sed quia non numquam eius modi tempora incidunt ut labore et dolore magnam aliquam quaerat voluptatem.</p>
        <p>Lorem ipsum dolor sit amet, consectetur adipisicing elit, sed do eiusmod tempor incididunt ut labore et dolore magna aliqua. Ut enim ad minim veniam, quis nostrud exercitation ullamco laboris nisi ut aliquip ex ea commodo consequat. Duis aute irure dolor in reprehenderit in voluptate</p>
      </div>
    </section>

    <div class="spine">
      <span class="spine-title">Lessons Taught by the Old Orchard Hives</span>
      <span class="spine-authors">Walter P. Kolb Ph. D.<br>Ruth P. Kolb</span>
    </div>

    <section class="front-cover">
      <div class="front-photo" role="img" aria-label="Close-up photograph of a honeybee gathering pollen on a bright yellow dandelion"></div>
      <h1 class="front-title">Lessons Taught<br>by the Old Orchard<span class="accent">Hives</span></h1>
      <p class="front-subtitle">A pocket guide to careful spending and caring for nature.</p>
    </section>

    <div class="author-band"></div>
    <p class="front-authors">Walter P. Kolb Ph. D.<span class="divider">|</span>Ruth P. Kolb</p>
  </div>
</body>
</html>
```